Business Card & Letterhead Design

We a financial advice company based in Australia. We provide advice to wealthy farmers.

We are changing our business name FROM Brightmere Financial TO Calderstone Wealth and we need a new letterhead and double sided business card design

Attached is designs from our previous branding (Brightmere Financial) as it includes all the details we require on the new Calderstone Wealth business cards and letterhead.

```html
<!DOCTYPE html>
<html lang="en">
<head>
<meta charset="utf-8">
<title>Calderstone Wealth – Stationery</title>
<link href="https://fonts.googleapis.com/css2?family=Cinzel:wght@400&family=Roboto:wght@400&family=Merriweather:wght@700&display=swap" rel="stylesheet">
<style>
  :root {
    --backdrop: #999999;
    --paper: #f7f7f5;
    --card-dark: #3d3d3d;
    --ink: #444444;
    --ink-soft: #5a5a5a;
    --faint: #ebebea;
    --faint-dark: #4a4a4a;
    --on-dark: #f2f2f2;
  }
  * { margin: 0; padding: 0; box-sizing: border-box; }
  html, body { width: 1200px; height: 1032px; overflow: hidden; background: var(--backdrop); }
  .canvas { position: relative; width: 1200px; height: 1032px; }
  .piece { position: absolute; overflow: hidden; }
  .letterhead { left: 447px; top: 74px; width: 625px; height: 883px; background: var(--paper); }
  .card-front { left: 127px; top: 330px; width: 270px; height: 163px; background: var(--card-dark); }
  .card-back { left: 127px; top: 537px; width: 270px; height: 163px; background: var(--paper); }

  .brand { position: absolute; text-align: center; color: var(--ink); }
  .brand-ring { display: block; margin: 0 auto; }
  .brand-name { font-family: "Cinzel", serif; font-weight: 400; white-space: nowrap; line-height: 1; }
  .brand-tagline { font-family: "Roboto", sans-serif; text-transform: uppercase; white-space: nowrap; line-height: 1; }

  .letterhead .brand { left: 40px; top: 42px; width: 190px; }
  .letterhead .brand-name { font-size: 15px; margin-top: 6px; letter-spacing: 0.2px; }
  .letterhead .brand-tagline { font-size: 6.6px; letter-spacing: 2.2px; margin-top: 2px; }

  .watermark { position: absolute; left: 117px; top: 245px; }

  .contact-block { position: absolute; left: 310px; top: 75px; width: 300px; font-family: "Roboto", sans-serif; font-size: 10.5px; color: var(--ink); }
  .contact-row { display: flex; align-items: center; gap: 10px; height: 17px; }
  .contact-row.gap { margin-top: 9px; }
  .contact-item { display: flex; align-items: center; gap: 4px; white-space: nowrap; }
  .icon { width: 10px; height: 10px; flex: none; }

  .card-front .brand { left: 60px; top: 46px; width: 150px; color: var(--on-dark); }
  .card-front .brand-name { font-size: 13.5px; margin-top: 4px; }
  .card-front .brand-tagline { font-size: 5.8px; letter-spacing: 2px; margin-top: 1px; }
  .front-ring { position: absolute; left: 176px; top: 4px; }

  .card-back .brand { left: 19px; top: 38px; width: 120px; }
  .card-back .brand-name { font-size: 11.5px; margin-top: 3px; }
  .card-back .brand-tagline { font-size: 4.6px; letter-spacing: 1.5px; margin-top: 1px; }

  .person { position: absolute; left: 157px; top: 23px; color: var(--ink); font-family: "Roboto", sans-serif; }
  .person-name { font-family: "Merriweather", serif; font-weight: 700; font-size: 8.5px; letter-spacing: 0.2px; }
  .person-title { font-size: 5.6px; line-height: 8px; color: var(--ink-soft); }
  .person-contacts { margin-top: 5px; font-size: 5.6px; line-height: 9.4px; color: var(--ink-soft); }
  .person-contacts li { list-style: none; display: flex; gap: 5px; align-items: flex-start; white-space: nowrap; }
  .person-contacts .icon { width: 6px; height: 6px; margin-top: 1.5px; }
  .person-contacts .cont { padding-left: 11px; }
</style>
</head>
<body>
<svg width="0" height="0" style="position:absolute">
  <defs>
    <symbol id="i-pin" viewBox="0 0 10 10"><circle cx="5" cy="5" r="4.5" fill="none" stroke="currentColor" stroke-width="0.8"/><path d="M5 2.2a1.9 1.9 0 0 0-1.9 1.9C3.1 5.5 5 7.8 5 7.8s1.9-2.3 1.9-3.7A1.9 1.9 0 0 0 5 2.2z" fill="currentColor"/><circle cx="5" cy="4.1" r="0.7" fill="#fff"/></symbol>
    <symbol id="i-phone" viewBox="0 0 10 10"><circle cx="5" cy="5" r="4.5" fill="none" stroke="currentColor" stroke-width="0.8"/><path d="M2.6 4.3c0-1 1.1-1.5 2.4-1.5s2.4.5 2.4 1.5L6.5 4.6 6.2 4c-.8-.3-1.6-.3-2.4 0L3.5 4.6zM3.4 5h3.2l.5 2.2H2.9z" fill="currentColor"/></symbol>
    <symbol id="i-fax" viewBox="0 0 10 10"><circle cx="5" cy="5" r="4.5" fill="none" stroke="currentColor" stroke-width="0.8"/><rect x="3.6" y="2.5" width="2.8" height="1.6" fill="currentColor"/><rect x="2.6" y="4.3" width="4.8" height="2.2" fill="currentColor"/><rect x="3.6" y="6.1" width="2.8" height="1.5" fill="currentColor"/></symbol>
    <symbol id="i-mobile" viewBox="0 0 10 10"><circle cx="5" cy="5" r="4.5" fill="none" stroke="currentColor" stroke-width="0.8"/><rect x="3.5" y="2.3" width="3" height="5.4" rx="0.5" fill="none" stroke="currentColor" stroke-width="0.8"/></symbol>
    <symbol id="i-mail" viewBox="0 0 10 10"><circle cx="5" cy="5" r="4.5" fill="none" stroke="currentColor" stroke-width="0.8"/><rect x="2.7" y="3.4" width="4.6" height="3.2" fill="currentColor"/><path d="M2.7 3.4 5 5.2l2.3-1.8" fill="none" stroke="#fff" stroke-width="0.5"/></symbol>
    <symbol id="i-web" viewBox="0 0 10 10"><circle cx="5" cy="5" r="4.5" fill="none" stroke="currentColor" stroke-width="0.8"/><circle cx="5" cy="5" r="2.5" fill="none" stroke="currentColor" stroke-width="0.6"/><path d="M2.5 5h5M5 2.5v5" stroke="currentColor" stroke-width="0.5"/></symbol>
  </defs>
</svg>

<main class="canvas">
  <section class="piece letterhead" aria-label="Letterhead">
    <div class="brand">
      <svg class="brand-ring" width="78" height="78" viewBox="0 0 78 78"><circle cx="39" cy="39" r="36.5" fill="none" stroke="var(--ink)" stroke-width="3"/></svg>
      <div class="brand-name">CALDERSTONE WEALTH</div>
      <div class="brand-tagline">Strategic Financial Advice</div>
    </div>

    <div class="contact-block">
      <div class="contact-row"><span class="contact-item"><svg class="icon"><use href="#i-pin"/></svg>PO Box 4218 Eastvale QLD 4170</span></div>
      <div class="contact-row"><span class="contact-item"><svg class="icon"><use href="#i-pin"/></svg>Suite 7A, 48 Marlow St Riverbend QLD 4170</span></div>
      <div class="contact-row gap">
        <span class="contact-item"><svg class="icon"><use href="#i-phone"/></svg>(07) 3200 1185</span>
        <span class="contact-item"><svg class="icon"><use href="#i-fax"/></svg>(07) 3200 1190</span>
        <span class="contact-item"><svg class="icon"><use href="#i-mobile"/></svg>0400 123 456</span>
      </div>
      <div class="contact-row">
        <span class="contact-item"><svg class="icon"><use href="#i-mail"/></svg>tom@brightmere.com.au</span>
        <span class="contact-item"><svg class="icon"><use href="#i-web"/></svg>brightmere.com.au</span>
      </div>
    </div>

    <svg class="watermark" width="396" height="396" viewBox="0 0 396 396" aria-hidden="true"><circle cx="198" cy="198" r="195" fill="none" stroke="var(--faint)" stroke-width="5"/></svg>
  </section>

  <section class="piece card-front" aria-label="Business card front">
    <svg class="front-ring" width="170" height="170" viewBox="0 0 170 170" aria-hidden="true"><circle cx="85" cy="85" r="82" fill="none" stroke="var(--faint-dark)" stroke-width="4"/></svg>
    <div class="brand">
      <svg class="brand-ring" width="46" height="46" viewBox="0 0 46 46"><circle cx="23" cy="23" r="21.5" fill="none" stroke="var(--on-dark)" stroke-width="2"/></svg>
      <div class="brand-name">CALDERSTONE WEALTH</div>
      <div class="brand-tagline">Strategic Financial Advice</div>
    </div>
  </section>

  <section class="piece card-back" aria-label="Business card back">
    <div class="brand">
      <svg class="brand-ring" width="52" height="52" viewBox="0 0 52 52"><circle cx="26" cy="26" r="24.8" fill="none" stroke="var(--ink)" stroke-width="2"/></svg>
      <div class="brand-name">CALDERSTONE WEALTH</div>
      <div class="brand-tagline">Strategic Financial Advice</div>
    </div>
    <div class="person">
      <div class="person-name">TOM REEVE</div>
      <div class="person-title">B.Ag.Ec. Dip F.P. CFP®<br>Managing Director</div>
      <ul class="person-contacts">
        <li><svg class="icon"><use href="#i-phone"/></svg>(07) 3200 1185</li>
        <li><svg class="icon"><use href="#i-mobile"/></svg>(07) 3200 1190</li>
        <li><svg class="icon"><use href="#i-fax"/></svg>0400 123 456</li>
        <li><svg class="icon"><use href="#i-mail"/></svg>tom@brightmere.com.au</li>
        <li><svg class="icon"><use href="#i-web"/></svg>www.brightmere.com.au</li>
        <li><svg class="icon"><use href="#i-pin"/></svg>Suite 7A, 48 Marlow St</li>
        <li class="cont">Riverbend QLD 4170</li>
        <li><svg class="icon"><use href="#i-pin"/></svg>PO Box 4218</li>
        <li class="cont">Eastvale QLD 4170</li>
      </ul>
    </div>
  </section>
</main>
</body>
</html>
```